British Columbia Day banner showcasing 20% off site

Banner graphic promoting our BC Day sale
Size: 1800 x 1000
- flag has been uploaded for inspiration
- examples from other companies and their sale banners have been uploaded for inspiration.
- product images can be found at www.mygreenleafhub.com, please use a variety of different products in this banner

Target Market(s)

19+

Industry/Entity Type

Cannabis

Requirements
Must have
• Phrases:
- “Celebrate BC Day with BC bud and companies”
- “20% off site wide sale*"
- Underneath phrase the date of sale “July 30th - August 3rd”
- In tiny print “*excludes all sale and bundled items”
- MUST BE 1800 X1000
Nice to have
• - images of the products or bud we carry which can be found at www.mygreenleafhub.com
- bold
Should not have
• - company logo

```html
<!DOCTYPE html>
<html lang="en">
<head>
<meta charset="utf-8">
<title>BC Day Sale Banner</title>
<link rel="stylesheet" href="https://fonts.googleapis.com/css2?family=Anton&family=Kanit:wght@400;500&display=swap">
<style>
  :root {
    --leaf-green: #8cc63f;
    --ink-black: #000000;
    --paper-white: #ffffff;
  }
  * { margin: 0; padding: 0; box-sizing: border-box; }
  html, body {
    width: 1200px;
    height: 670px;
    overflow: hidden;
    background: var(--ink-black);
  }
  .banner {
    position: relative;
    width: 1200px;
    height: 670px;
    background: var(--ink-black);
    overflow: hidden;
  }
  .banner__shapes {
    position: absolute;
    inset: 0;
    width: 1200px;
    height: 670px;
  }
  .banner__shapes .panel { fill: var(--leaf-green); }

  .brand-name {
    position: absolute;
    left: 76px;
    top: 150px;
    font-family: "Kanit", sans-serif;
    font-weight: 500;
    font-size: 34px;
    color: var(--paper-white);
    letter-spacing: 0.5px;
  }

  .headline {
    position: absolute;
    right: 56px;
    top: 82px;
    text-align: right;
    font-family: "Anton", sans-serif;
    font-weight: 400;
    font-size: 50px;
    line-height: 64px;
    color: var(--ink-black);
    letter-spacing: 0.3px;
  }

  .sale-dates {
    position: absolute;
    right: 56px;
    top: 346px;
    font-family: "Anton", sans-serif;
    font-size: 42px;
    line-height: 60px;
    color: var(--leaf-green);
  }

  .fine-print {
    position: absolute;
    right: 56px;
    top: 474px;
    font-family: "Kanit", sans-serif;
    font-weight: 400;
    font-size: 22px;
    color: var(--ink-black);
  }

  .offer {
    position: absolute;
    left: 70px;
    top: 338px;
    color: var(--leaf-green);
    font-family: "Anton", sans-serif;
  }
  .offer__percent {
    display: block;
    font-size: 184px;
    line-height: 190px;
  }
  .offer__label {
    display: block;
    font-size: 90px;
    line-height: 100px;
    margin-top: -8px;
    letter-spacing: 0.5px;
  }
  .offer__label sup {
    font-size: 60px;
    vertical-align: 30px;
    line-height: 0;
  }
</style>
</head>
<body>
  <main class="banner">
    <svg class="banner__shapes" viewBox="0 0 1200 670" aria-hidden="true">
      <polygon class="panel panel--top" points="453,0 1200,0 1200,328 628,328"/>
      <polygon class="panel panel--bottom" points="680,426 1200,426 1200,670 810,670"/>
    </svg>

    <div class="brand-name">GreenLeafHub</div>

    <h1 class="headline">Celebrate BC Day with<br>BC bud and companies</h1>

    <p class="sale-dates">July 30th - August 3rd</p>

    <p class="fine-print">*excludes all sale and bundled items</p>

    <p class="offer">
      <span class="offer__percent">20%</span>
      <span class="offer__label">off site wide sale<sup>*</sup></span>
    </p>
  </main>
</body>
</html>
```